BrivoMatex. Lantern for the Steady Growth. Business card

Professional business card for BrivoMatex (Lantern for the Steady Growth)
My rationale: Strategy-> Execution-> Results-> Value that lead to the BrivoMatex name: We put the Lantern for the Steady Growth.
We deliver value to our customers helping them at defining a good strategy (cyan arrow). 90% of well formulated strategies fail due to poor execution so we also consider strategical execution very important (green arrow). Due to the execution we obtain the results (blue arrow). Finally, the results provide feedback to redefine strategy, and the new strategy has to be executed and new results obtained providing new feedback and on and on. It's like a wheel that finally, must create corporate value: value for shareholders, staholders, employees, providers...-

Target Market(s)

CEOs and steering comitees , invewrnent funds

Industry/Entity Type

Business Consultant

Contact Information for Business Card

Tommaso Ferlini
CEO & Founder
tommaso.ferlini@brivomatex.example
Mobile: +34 611.205.938
www.brivomatex.example

Colors

Designer to choose colors to be used in the design.

Requirements
Nice to have
• Nice to hace the words: Strategy, execution, results
• Nice to vave the claim: Lantern for the Steady Growth
• The three colors should be shown:
• cyan for STRATEGY
• green for EXECUTION
• blue for RESULTS
Should not have
• Complete black background

```html
<!DOCTYPE html>
<html lang="en">
<head>
<meta charset="UTF-8">
<title>BrivoMatex – Business Card</title>
<link href="https://fonts.googleapis.com/css2?family=Montserrat:wght@600;700&family=Roboto:wght@400&display=swap" rel="stylesheet">
<style>
  :root {
    --page-grey: #d9d8d5;
    --card-black: #050607;
    --card-sheen: #222325;
    --brand-blue: #2a45a8;
    --brand-green: #9dd23c;
    --brand-cyan: #27b4e8;
    --text-white: #f2f2f2;
  }
  * { margin: 0; padding: 0; box-sizing: border-box; }
  html, body { width: 1200px; height: 801px; overflow: hidden; }
  body {
    background: var(--page-grey);
    display: flex;
    flex-direction: column;
    align-items: center;
    justify-content: center;
    gap: 21px;
  }

  .card {
    position: relative;
    width: 640px;
    height: 366px;
    background: radial-gradient(ellipse at 75% 0%, var(--card-sheen) 0%, var(--card-black) 60%);
    overflow: hidden;
    box-shadow: 0 6px 18px rgba(0,0,0,0.25);
  }

  /* Front side */
  .brand {
    position: absolute;
    left: 40px;
    top: 158px;
    display: flex;
    align-items: center;
    gap: 10px;
  }
  .brand-dot {
    width: 14px; height: 14px;
    border-radius: 50%;
    background: var(--brand-blue);
  }
  .brand-name {
    font-family: "Montserrat", sans-serif;
    font-weight: 700;
    font-size: 36px;
    letter-spacing: -0.5px;
    color: var(--brand-blue);
    line-height: 1;
  }

  .divider {
    position: absolute;
    left: 305px;
    top: 88px;
    width: 2px;
    height: 180px;
    background: var(--brand-cyan);
  }

  .contact {
    position: absolute;
    left: 328px;
    top: 96px;
  }
  .person-name {
    font-family: "Montserrat", sans-serif;
    font-weight: 700;
    font-size: 24px;
    color: var(--brand-blue);
    line-height: 1.1;
  }
  .person-title {
    font-family: "Montserrat", sans-serif;
    font-weight: 600;
    font-size: 17px;
    color: var(--brand-green);
    margin-top: 3px;
  }
  .details {
    list-style: none;
    margin-top: 22px;
    font-family: "Roboto", sans-serif;
    font-size: 14px;
    color: var(--text-white);
  }
  .details li {
    display: flex;
    align-items: center;
    gap: 8px;
    height: 22px;
  }
  .details svg { width: 14px; height: 14px; flex: none; }

  .stripe {
    position: absolute;
    left: 0; bottom: 0;
    width: 100%;
    height: 10px;
    display: flex;
  }
  .stripe-results { width: 36%; background: var(--brand-blue); }
  .stripe-execution { width: 32%; background: var(--brand-green); }
  .stripe-strategy { width: 32%; background: var(--brand-cyan); }

  /* Back side */
  .card-back {
    background: radial-gradient(ellipse at 60% 40%, #0b0e14 0%, var(--card-black) 70%);
  }
  .back-brand {
    position: absolute;
    inset: 0;
    display: flex;
    align-items: center;
    justify-content: center;
    gap: 16px;
    padding-top: 40px;
  }
  .back-brand .brand-dot { width: 26px; height: 26px; }
  .back-brand .brand-name { font-size: 72px; letter-spacing: -1px; }
</style>
</head>
<body>
  <main class="card card-front">
    <div class="brand">
      <span class="brand-dot"></span>
      <span class="brand-name">BrivoMatex</span>
    </div>

    <div class="divider"></div>

    <section class="contact">
      <h1 class="person-name">Tommaso Ferlini</h1>
      <p class="person-title">CEO &amp; Founder</p>
      <ul class="details">
        <li>
          <svg viewBox="0 0 26 26" aria-hidden="true"><rect x="7" y="2" width="12" height="22" rx="2" fill="none" stroke="var(--brand-green)" stroke-width="2.4"/><circle cx="13" cy="20" r="1.5" fill="var(--brand-green)"/></svg>
          <span>+34 611.205.938</span>
        </li>
        <li>
          <svg viewBox="0 0 26 26" aria-hidden="true"><rect x="2" y="5" width="22" height="16" fill="var(--brand-green)"/><path d="M2 5 L13 14 L24 5 M2 21 L10 12 M24 21 L16 12" fill="none" stroke="var(--card-black)" stroke-width="1.8"/></svg>
          <span>tommaso.ferlini@brivomatex.example</span>
        </li>
        <li>
          <svg viewBox="0 0 26 26" aria-hidden="true"><circle cx="13" cy="13" r="11" fill="var(--brand-green)"/><path d="M2 13 H24 M13 2 C7 8 7 18 13 24 M13 2 C19 8 19 18 13 24" fill="none" stroke="var(--card-black)" stroke-width="1.6"/></svg>
          <span>www.brivomatex.example</span>
        </li>
      </ul>
    </section>

    <div class="stripe">
      <span class="stripe-results"></span>
      <span class="stripe-execution"></span>
      <span class="stripe-strategy"></span>
    </div>
  </main>

  <section class="card card-back">
    <div class="back-brand">
      <span class="brand-dot"></span>
      <span class="brand-name">BrivoMatex</span>
    </div>
  </section>
</body>
</html>
```